Business cards - KESTO Roofing & Siding

We need simple business cards made up for our Roofing & Siding business based in Calgary Alberta.
The logo on one side of the card and potentially our slogan "Built to last, proven every season".
The other side could have:
-A small logo
-Rep name:
-Rep cell phone:
-Rep email:
-Office phone: 403-386-2049
-Website: PrairieShinglePros.com

We would like to incorporate the colours from our logo, especially the lite blue on the jpeg file. I have attached the ai file and jpeg file. We like the colours better on the jpeg file.

I do not require a money back guarantee

```html
<!DOCTYPE html>
<html lang="en">
<head>
<meta charset="utf-8">
<title>KESTO Roofing &amp; Siding – Business Cards</title>
<link href="https://fonts.googleapis.com/css2?family=Roboto:wght@400;500&family=Titillium+Web:wght@400;600&display=swap" rel="stylesheet">
<style>
  :root {
    --red: #ec2227;
    --blue: #4282c4;
    --navy: #1d2f6f;
    --ink: #000000;
    --paper: #ffffff;
    --grey: #8a8a8a;
    --stage: #e6e7ea;
  }
  html, body {
    margin: 0;
    width: 991px;
    height: 1200px;
    overflow: hidden;
    background: var(--stage);
  }
  .card {
    position: absolute;
    left: 128px;
    width: 734px;
    height: 420px;
    overflow: hidden;
  }
  .card--front { top: 113px; background: var(--ink); }
  .card--back { top: 676px; background: var(--paper); }

  .band { position: absolute; height: 15px; }
  .band--red { background: var(--red); }
  .band--blue { background: var(--blue); }

  .brand {
    position: absolute;
    left: 0; right: 0;
    display: flex;
    justify-content: center;
    align-items: center;
    gap: 12px;
    font-family: "Titillium Web", sans-serif;
    font-weight: 600;
    letter-spacing: 0.06em;
    white-space: nowrap;
  }
  .brand__square { width: 18px; height: 18px; background: var(--blue); }

  .card--front .brand { top: 210px; font-size: 34px; color: var(--paper); }
  .slogan {
    position: absolute;
    top: 315px; left: 0; right: 0;
    margin: 0;
    text-align: center;
    font-family: "Titillium Web", sans-serif;
    font-weight: 400;
    font-size: 14px;
    letter-spacing: 0.24em;
    color: var(--paper);
  }

  .card--back .brand {
    top: 212px; left: 20px; right: auto; width: 340px;
    font-size: 22px; color: var(--ink); gap: 10px;
  }
  .divider {
    position: absolute;
    left: 367px; top: 117px;
    width: 1px; height: 185px;
    background: #b5b5b5;
  }
  .rep {
    position: absolute;
    left: 406px; top: 100px;
    font-family: "Roboto", sans-serif;
  }
  .rep__name { margin: 0; font-size: 28px; font-weight: 500; line-height: 1.1; color: var(--ink); }
  .rep__title { margin: 0; font-size: 13px; color: var(--navy); }

  .contact {
    position: absolute;
    left: 406px; top: 0;
    margin: 0; padding: 0;
    list-style: none;
    font-family: "Roboto", sans-serif;
    font-size: 14.5px;
    line-height: 17px;
    color: var(--ink);
  }
  .contact__item { position: absolute; left: 0; display: flex; align-items: center; gap: 19px; white-space: nowrap; }
  .contact__item--phone { top: 180px; }
  .contact__item--mail { top: 222px; }
  .contact__item--web { top: 265px; }
  .contact__icon { width: 28px; height: 28px; flex: none; }
</style>
</head>
<body>

<section class="card card--front" aria-label="Card front">
  <div class="band band--red" style="left:0;top:0;width:194px"></div>
  <div class="band band--blue" style="left:206px;top:0;right:0"></div>

  <div class="brand"><span class="brand__square"></span>KESTO Roofing &amp; Siding</div>
  <p class="slogan">BUILT TO LAST, PROVEN EVERY SEASON</p>

  <div class="band band--blue" style="left:0;bottom:0;width:528px"></div>
  <div class="band band--red" style="left:540px;bottom:0;right:0"></div>
</section>

<section class="card card--back" aria-label="Card back">
  <div class="brand"><span class="brand__square"></span>KESTO Roofing &amp; Siding</div>
  <div class="divider"></div>

  <div class="rep">
    <p class="rep__name">Your Name</p>
    <p class="rep__title">Project Manager</p>
  </div>

  <ul class="contact">
    <li class="contact__item contact__item--phone">
      <svg class="contact__icon" viewBox="0 0 28 28" aria-hidden="true">
        <circle cx="14" cy="14" r="14" fill="#9a9a9a"/>
        <path d="M9.5 7.5c1-.6 1.8-.3 2.3.6l1 2c.3.7.1 1.3-.5 1.7l-.9.6c.6 1.7 1.9 3.2 3.5 4l.7-.9c.5-.5 1.100-.6 1.7-.3l2 1.1c.8.5 1 1.3.4 2.2-1 1.6-2.800 2-4.600 1.1-3.300-1.600-5.700-4.300-6.900-7.600-.6-1.800-.1-3.600 1.300-4.500z" fill="#fff"/>
      </svg>
      <span>+00 1234 567 8900<br>403-386-2049</span>
    </li>
    <li class="contact__item contact__item--mail">
      <svg class="contact__icon" viewBox="0 0 28 28" aria-hidden="true">
        <circle cx="14" cy="14" r="14" fill="#9a9a9a"/>
        <rect x="7" y="9" width="14" height="10" fill="none" stroke="#fff" stroke-width="1.3"/>
        <path d="M7 9l7 6 7-6M7 19l5-5M21 19l-5-5" fill="none" stroke="#fff" stroke-width="1.3"/>
      </svg>
      <span>yourmailadress@domain.com<br>secondmail@domain.com</span>
    </li>
    <li class="contact__item contact__item--web">
      <svg class="contact__icon" viewBox="0 0 28 28" aria-hidden="true">
        <circle cx="14" cy="14" r="14" fill="#9a9a9a"/>
        <g fill="none" stroke="#fff" stroke-width="1.2">
          <circle cx="14" cy="14" r="7.5"/>
          <ellipse cx="14" cy="14" rx="3.3" ry="7.5"/>
          <path d="M6.5 14h15M7.5 10.5h13M7.5 17.5h13M14 6.5v15"/>
        </g>
      </svg>
      <span>PrairieShinglePros.com</span>
    </li>
  </ul>

  <div class="band band--blue" style="left:0;bottom:0;width:528px"></div>
  <div class="band band--red" style="left:540px;bottom:0;right:0"></div>
</section>

</body>
</html>
```